Business card design needed

I have started a new business called Marlow Auto Electrical, although the words Marlow Auto Electrical will be used on signage and documents I actually want to market the business as MAE. The services I offer are Mobile Auto Electrical, Automotive Air Conditioning and Test And Tag. My business will be targetting the Mining Industry, Civil, Rail, Agricultural and Workshop Testing And Tagging. My auto electrical service ranges from fault finding to new vehicle and mine compliance fit outs. I have a very strong focus on quality workmanship. I will upload the logo I have designed and want to use I am happy for the logo colour to change but the design itself must stay the same. I want the design to have a modern, eye catching, energetic feel. As I am a passionate motorsport fan I am happy for this to also influence the design. I am happy for the front of the card to have only the emblem and logo design and the back to have all the info.

Industry/Entity Type

Electrical

Contact Information for Business Card

MAE Marlow Auto Electrical, Dale Penrick, Auto Electrician, Mobile No 0417263859

Requirements
Must have
• On the business card it is mandatory that the following license numbers are shown:

MVRL38462
VDA L071348
ABN 61 839 204 518

```html
<!DOCTYPE html>
<html lang="en">
<head>
<meta charset="utf-8">
<title>Marlow Auto Electrical – Business Card</title>
<link rel="stylesheet" href="https://fonts.googleapis.com/css2?family=Titillium+Web:wght@400;600;700&display=swap">
<style>
  :root {
    --stage: #6f6f6f;
    --card-dark: #1f1f1f;
    --card-dark-edge: #181818;
    --red: #b8372a;
    --red-deep: #8c1f17;
    --brand-red: #d0392b;
    --white: #ffffff;
    --soft-white: #f3dcd8;
    --muted-red-text: #3d0f0b;
    --licence-grey: #d6d6d6;
  }
  * { margin: 0; padding: 0; box-sizing: border-box; }
  html, body {
    width: 1200px;
    height: 949px;
    overflow: hidden;
    background: var(--stage);
    font-family: "Titillium Web", sans-serif;
  }
  .sheet {
    width: 1200px;
    height: 949px;
    display: flex;
    flex-direction: column;
    align-items: center;
    justify-content: center;
    gap: 44px;
  }
  .card {
    position: relative;
    width: 700px;
    height: 389px;
    background: linear-gradient(160deg, var(--card-dark), var(--card-dark-edge));
    box-shadow: 0 10px 28px rgba(0, 0, 0, 0.45);
    overflow: hidden;
  }
  .card__bands {
    position: absolute;
    inset: 0;
    width: 100%;
    height: 100%;
  }
  .brand {
    position: absolute;
    text-align: center;
  }
  .brand__mark {
    display: block;
    color: var(--brand-red);
    font-weight: 700;
    line-height: 0.9;
    letter-spacing: 2px;
  }
  .brand__name {
    display: block;
    color: var(--white);
    font-weight: 600;
    line-height: 1.2;
  }
  /* Details side */
  .card--details .brand {
    top: 48px;
    right: 58px;
  }
  .card--details .brand__mark { font-size: 92px; }
  .card--details .brand__name { font-size: 24px; }
  .licences {
    position: absolute;
    right: 52px;
    top: 200px;
    text-align: right;
    color: var(--licence-grey);
    font-size: 19px;
    line-height: 1.3;
    letter-spacing: 0.5px;
  }
  .contact {
    position: absolute;
    left: 40px;
    bottom: 44px;
  }
  .contact__name {
    color: var(--white);
    font-weight: 600;
    font-size: 30px;
    line-height: 1.1;
  }
  .contact__role {
    color: var(--muted-red-text);
    font-size: 25px;
    line-height: 1.2;
  }
  .contact__mobile {
    color: var(--soft-white);
    font-size: 25px;
    line-height: 1.2;
  }
  /* Emblem side */
  .card--emblem .brand {
    left: 0;
    right: 0;
    top: 112px;
  }
  .card--emblem .brand__mark { font-size: 118px; }
  .card--emblem .brand__name { font-size: 29px; }
</style>
</head>
<body>
<main class="sheet">
  <section class="card card--details" aria-label="Card details side">
    <svg class="card__bands" viewBox="0 0 700 389" preserveAspectRatio="none" aria-hidden="true">
      <polygon points="150,0 210,0 460,389 420,389" fill="var(--red-deep)"/>
      <polygon points="0,0 150,0 420,389 0,389" fill="var(--red)"/>
    </svg>
    <div class="brand">
      <span class="brand__mark">MAE</span>
      <span class="brand__name">Marlow Auto Electrical</span>
    </div>
    <div class="licences">
      <p>MVRL38462</p>
      <p>VDA L071348</p>
      <p>ABN 61 839 204 518</p>
    </div>
    <div class="contact">
      <p class="contact__name">Dale Penrick</p>
      <p class="contact__role">Auto Electrician</p>
      <p class="contact__mobile">Mobile: 0417 263 859</p>
    </div>
  </section>

  <section class="card card--emblem" aria-label="Card emblem side">
    <div class="brand">
      <span class="brand__mark">MAE</span>
      <span class="brand__name">Marlow Auto Electrical</span>
    </div>
  </section>
</main>
</body>
</html>
```